Commercial Bakery needs packing design for a Bread Bag.

Brenton's Bakery needs a design for a bread bag to be distributed to grocery stores. We make all kinds of breads and want this packaging to represent our company. We would like the packaging to be black and white with a fun/bubbly modern design. I have attached a few ideas of what I am looking for.
There are 5 different products. Packaging must be the same for each product except for corresponding product name, bar code and nutrional facts.
Product names:
Coconut Cream Bread
Cream Bread
Potato Rolls
Roll ups
Coconut & Raisin Bread

Our products are packaged in a 11” x 8” poly bag.
I will open 5 contracts with whoever’s design I select. I will then provide nutritional facts, barcodes for items once a contract is selected. Thank you!!

Target Market(s)

Grocery stores

Industry/Entity Type

Bakery

Requirements
Must have
• Black and White (off whites are ok)
Should not have
• Color

```html
<!DOCTYPE html>
<html lang="en">
<head>
<meta charset="utf-8">
<title>Brenton's Bakery – Bread Bag</title>
<link rel="stylesheet" href="https://fonts.googleapis.com/css2?family=Montserrat:wght@500;700&family=Pacifico&display=swap">
<style>
  :root {
    --backdrop: #d6d6d3;
    --ink: #1b1b1b;
    --paper: #ffffff;
    --offwhite: #f3f1ec;
    --dot-field-light: #9a9a9a;
    --dot-field-dark: #7a7a7a;
  }
  html, body {
    margin: 0;
    padding: 0;
    width: 1200px;
    height: 894px;
    overflow: hidden;
    background: var(--backdrop);
  }
  .bag-artwork {
    display: block;
    width: 1200px;
    height: 894px;
  }
  .ink { fill: var(--ink); }
  .paper { fill: var(--paper); }
  .seam-line { fill: var(--offwhite); }
  .brand-name {
    font-family: "Pacifico", cursive;
    font-weight: 400;
    font-size: 22px;
    fill: var(--ink);
  }
  .product-name {
    font-family: "Montserrat", sans-serif;
    font-weight: 700;
    font-size: 19px;
    letter-spacing: 1.5px;
    text-transform: uppercase;
    fill: var(--offwhite);
  }
</style>
</head>
<body>
<svg class="bag-artwork" viewBox="0 0 1206 898" xmlns="http://www.w3.org/2000/svg">
  <defs>
    <radialGradient id="dot-field" cx="50%" cy="40%" r="75%">
      <stop offset="0%" stop-color="#9a9a9a"/>
      <stop offset="100%" stop-color="#7a7a7a"/>
    </radialGradient>

    <g id="front-face">
      <g role="img" aria-label="Grey bubble dot pattern">
        <rect x="0" y="0" width="252" height="627" fill="url(#dot-field)"/>
      </g>
      <rect class="paper" x="75" y="0" width="102" height="627"/>
      <circle class="paper" cx="127" cy="326" r="96"/>
      <text class="brand-name" x="127" y="334" text-anchor="middle">Brenton's Bakery</text>
      <path class="ink" d="M0,430 C70,448 120,490 170,490 C210,490 235,470 252,460 L252,478 C225,492 200,505 160,505 C110,505 55,475 0,462 Z"/>
      <path class="seam-line" d="M0,462 C55,475 110,505 160,505 C200,505 225,492 252,478 L252,484 C225,498 200,511 160,511 C110,511 55,481 0,468 Z"/>
      <path class="ink" d="M0,468 C55,481 110,517 160,517 C200,517 225,500 252,490 L252,627 L0,627 Z"/>
    </g>
  </defs>

  <!-- left bag -->
  <rect class="ink" x="163" y="135" width="188" height="627"/>
  <use href="#front-face" x="351" y="135"/>
  <text class="product-name" x="477" y="706" text-anchor="middle">Cream Bread</text>

  <!-- right bag -->
  <rect class="ink" x="603" y="135" width="188" height="627"/>
  <use href="#front-face" x="790" y="135"/>
  <text class="product-name" x="916" y="706" text-anchor="middle">Potato Rolls</text>
</svg>
</body>
</html>
```